Come as U R - mental health service LGBTIQ inclusive poster

We are a mental health organisation in Australia that is looking for a poster design that we can put in our waiting rooms to show that our service is inclusive of gender diverse, intersex, and sexuality diverse people. We will add text and our company logo afterwards. An example has been provided for inspiration. Designers 25 and under encouraged.

Target Market(s)

Target audience - all genders 12-25.

Industry/Entity Type

Mental Health

Requirements
Must have
• This graphic should be colourful, include the text "Come as U R", and incorporate the colours of the pride flag. Should be a general design that is appropriate for all of the target audience.

```html
<!DOCTYPE html>
<html lang="en">
<head>
<meta charset="utf-8">
<title>Come as U R — Inclusive Waiting Room Poster</title>
<link rel="stylesheet" href="https://fonts.googleapis.com/css2?family=Questrial&family=Russo+One&display=swap">
<style>
  :root {
    --canvas-bg: #e9e8e4;
    --paper: #ffffff;
    --paper-shade: #e4e4e4;
    --ink: #0d0d0d;
    --ink-soft: #3a3a3a;
    --art-light: #eef0e6;
    --art-mid: #b9bcb2;
    --art-dark: #2a2a2a;
    --pride-red: #e40303;
    --pride-orange: #ff8c00;
    --pride-yellow: #ffed00;
    --pride-green: #008026;
    --pride-blue: #004dff;
    --pride-violet: #a000c8;
    --pride-magenta: #d0189a;
  }
  html, body {
    margin: 0;
    width: 1200px;
    height: 1000px;
    overflow: hidden;
    background: var(--canvas-bg);
  }
  .canvas {
    position: relative;
    width: 1200px;
    height: 1000px;
  }
  .poster {
    position: absolute;
    left: 280px;
    top: 30px;
    width: 640px;
    height: 940px;
    background: var(--paper);
    box-shadow: 0 6px 18px rgba(0,0,0,.18);
    overflow: hidden;
  }
  .poster svg { display: block; }
  .word-come {
    font-family: "Questrial", "Century Gothic", sans-serif;
    fill: var(--ink);
  }
  .block-letter {
    font-family: "Russo One", "Arial Black", sans-serif;
  }
  .plus-sign {
    stroke: var(--ink-soft);
    stroke-width: 4;
  }
</style>
</head>
<body>
<main class="canvas">
  <section class="poster" aria-label="Come as U R poster">
    <svg width="640" height="940" viewBox="0 0 640 940" xmlns="http://www.w3.org/2000/svg">
      <defs>
        <radialGradient id="paper-glow" cx="45%" cy="50%" r="70%">
          <stop offset="0" stop-color="#ffffff"/>
          <stop offset="1" stop-color="var(--paper-shade)"/>
        </radialGradient>
        <linearGradient id="art-top-tone" x1="0" y1="0" x2="1" y2="1">
          <stop offset="0" stop-color="var(--art-mid)"/>
          <stop offset=".45" stop-color="var(--art-light)"/>
          <stop offset="1" stop-color="var(--art-dark)"/>
        </linearGradient>
        <linearGradient id="art-bottom-tone" x1="0" y1="1" x2="1" y2="0">
          <stop offset="0" stop-color="var(--art-light)"/>
          <stop offset=".5" stop-color="var(--art-mid)"/>
          <stop offset="1" stop-color="var(--art-dark)"/>
        </linearGradient>
        <linearGradient id="pride-rainbow" x1="0" y1="0" x2="1" y2="1">
          <stop offset="0" stop-color="var(--pride-magenta)"/>
          <stop offset=".22" stop-color="var(--pride-violet)"/>
          <stop offset=".4" stop-color="var(--pride-blue)"/>
          <stop offset=".56" stop-color="var(--pride-green)"/>
          <stop offset=".7" stop-color="var(--pride-yellow)"/>
          <stop offset=".84" stop-color="var(--pride-orange)"/>
          <stop offset="1" stop-color="var(--pride-red)"/>
        </linearGradient>
        <linearGradient id="block-steel" x1="0" y1="0" x2="0" y2="1">
          <stop offset="0" stop-color="#6a6a6a"/>
          <stop offset=".5" stop-color="#1c1c1c"/>
          <stop offset="1" stop-color="#050505"/>
        </linearGradient>
        <filter id="soft-shadow" x="-20%" y="-20%" width="140%" height="140%">
          <feDropShadow dx="0" dy="4" stdDeviation="5" flood-color="#000" flood-opacity=".35"/>
        </filter>
      </defs>

      <rect class="paper-ground" width="640" height="940" fill="url(#paper-glow)"/>

      <g class="torn-art torn-art--top" filter="url(#soft-shadow)">
        <path fill="#ffffff" d="M0 0 H640 V34 L620 40 L600 38 L575 52 L550 50 L520 66 L495 64 L465 82 L440 80 L410 98 L385 96 L355 116 L330 114 L300 134 L272 132 L245 152 L218 150 L190 170 L160 170 L135 190 L108 190 L80 210 L52 212 L28 232 L0 240 Z"/>
        <path role="img" aria-label="Torn strip of an ink-wash portrait illustration" fill="url(#art-top-tone)" d="M0 0 H640 V22 L612 28 L590 26 L565 40 L540 38 L510 54 L485 52 L455 70 L430 68 L400 86 L375 84 L345 104 L320 102 L290 122 L262 120 L235 140 L208 138 L180 158 L150 158 L125 178 L98 178 L70 198 L42 200 L18 220 L0 226 Z"/>
      </g>

      <g class="torn-art torn-art--bottom" filter="url(#soft-shadow)">
        <path fill="#ffffff" d="M0 790 L24 780 L50 782 L78 766 L104 768 L132 750 L160 752 L188 732 L215 734 L242 714 L270 716 L298 694 L325 696 L352 674 L380 676 L408 652 L435 654 L462 630 L490 630 L516 606 L544 604 L570 578 L598 574 L620 548 L640 540 V940 H0 Z"/>
        <path role="img" aria-label="Torn strip of an ink-wash portrait illustration" fill="url(#art-bottom-tone)" d="M0 804 L24 794 L50 796 L78 780 L104 782 L132 764 L160 766 L188 746 L215 748 L242 728 L270 730 L298 708 L325 710 L352 688 L380 690 L408 666 L435 668 L462 644 L490 644 L516 620 L544 618 L570 592 L598 588 L620 562 L640 554 V940 H0 Z"/>
      </g>

      <g class="headline-come" transform="translate(66 462) rotate(-21) scale(0.9)">
        <text class="word-come" x="0" y="0" font-size="220">C</text>
        <path class="pride-heart" transform="translate(150 -165) scale(1.55)"
              d="M50 90 C20 70 0 50 0 28 C0 12 12 0 27 0 C38 0 46 6 50 15 C54 6 62 0 73 0 C88 0 100 12 100 28 C100 50 80 70 50 90Z"
              fill="url(#pride-rainbow)" stroke="var(--ink)" stroke-width="6" stroke-linejoin="round"/>
        <text class="word-come" x="312" y="0" font-size="220">ME</text>
      </g>

      <text class="block-letter word-as" x="400" y="452" font-size="130"
            fill="var(--ink)" stroke="#ffffff" stroke-width="5" paint-order="stroke"
            filter="url(#soft-shadow)">AS</text>

      <text class="block-letter word-u" x="62" y="700" font-size="255"
            fill="url(#block-steel)" filter="url(#soft-shadow)">U</text>
      <g class="plus-sign">
        <line x1="335" y1="574" x2="335" y2="684"/>
        <line x1="282" y1="629" x2="388" y2="629"/>
      </g>
      <text class="block-letter word-r" x="444" y="898" font-size="250"
            textLength="150" lengthAdjust="spacingAndGlyphs"
            fill="var(--ink)" stroke="#ffffff" stroke-width="6" paint-order="stroke"
            filter="url(#soft-shadow)">R</text>
    </svg>
  </section>
</main>
</body>
</html>
```